New Solo Law Office Needs Business Card/Letterhead Design

I am starting a solo law office called "Law Office of Brian Kolmer, PLLC" in Tucson, Arizona. I will be doing criminal defense trial work. More than a logo with any sort of icon, I am really just looking for the name of the company to be displayed in a sleek, minimalist but interesting sort of way, with a format and font type that communicates professionalism. It can be in color, but doesn't have to be, and I am thinking blue and/or red accents colors. I'd like it to convey that I am passionate, dependable and willing to fight. For the business card, I envision sort of higher quality card material, and maybe some embossing or raised print. I will want to include my company name, name, phone and fax numbers, email and website addresses. For the letterhead, I will want to be able to use the same sort of font/formatting design as on the business card.
Industry/Entity Type
Business
Contact Information for Business Card
Law Office of Brian Kolmer, PLLC
Brian Kolmer
brian@kolmer-law.example
www.kolmer-law.example
(I do not yet have an established phone or fax number, so please put in some place holder numbers for the formatting, and I can add the actual numbers in before I print.)
Colors
Designer to choose colors to be used in the design.
Look and feel
Each slider illustrates characteristics of the customer's brand and the style your logo design should communicate.

```html
<!DOCTYPE html>
<html lang="en">
<head>
<meta charset="utf-8">
<title>Law Office of Brian Kolmer, PLLC – Business Card</title>
<link rel="stylesheet" href="https://fonts.googleapis.com/css2?family=Cinzel:wght@400;700&family=Roboto:wght@400&display=swap">
<style>
  :root {
    --page-bg: #cfcfcf;
    --page-bg-light: #e6e6e6;
    --navy: #342b8a;
    --navy-faint: #3f379a;
    --red: #a8212a;
    --coral: #e0525a;
    --white: #ffffff;
    --rule: #c8c8c8;
    --ink: #1e1e1e;
  }
  * { margin: 0; padding: 0; box-sizing: border-box; }
  html, body { width: 900px; height: 1200px; overflow: hidden; }
  body {
    background: radial-gradient(ellipse at center, var(--page-bg-light) 0%, var(--page-bg) 75%);
    position: relative;
    font-family: "Cinzel", serif;
  }
  .card {
    position: absolute;
    left: 70px;
    width: 760px;
    height: 444px;
    box-shadow: 0 3px 8px rgba(0,0,0,0.35);
    overflow: hidden;
  }
  .card--front { top: 120px; background: var(--navy); }
  .card--back {
    top: 628px;
    background: linear-gradient(to bottom, var(--white) 55%, #f1f1f1 100%);
  }
  .backdrop-shape {
    position: absolute;
    left: 230px; top: 140px;
    width: 560px; height: 400px;
  }
  .brand {
    position: absolute;
    display: flex;
    align-items: center;
  }
  .card--front .brand { left: 92px; top: 176px; }
  .card--back .brand { left: 120px; top: 160px; }
  .brand__mark {
    width: 64px; height: 64px;
    border-radius: 50%;
    margin-right: 54px;
  }
  .card--front .brand__mark { background: var(--white); }
  .card--back .brand__mark { background: var(--navy); }
  .brand__rule { width: 1px; height: 86px; margin-right: 14px; }
  .card--front .brand__rule { background: rgba(255,255,255,0.7); }
  .card--back .brand__rule { background: var(--rule); }
  .brand__text { line-height: 1; }
  .brand__lead { font-size: 27px; letter-spacing: 0.5px; display: block; }
  .brand__name { font-size: 33px; letter-spacing: 0.5px; display: block; margin-top: 8px; }
  .brand__place { font-size: 17px; letter-spacing: 0.5px; display: block; margin-top: 8px; }
  .card--front .brand__lead,
  .card--front .brand__name { color: var(--white); }
  .card--front .brand__place { color: var(--coral); }
  .card--back .brand__lead { color: var(--red); }
  .card--back .brand__name { color: var(--navy); }
  .card--back .brand__place { color: var(--coral); }

  .person {
    position: absolute;
    left: 0; width: 760px;
    top: 278px;
    text-align: center;
  }
  .person__name { font-size: 26px; font-weight: 700; color: var(--navy); letter-spacing: 0.5px; line-height: 1; }
  .person__role { font-size: 14px; font-weight: 700; color: var(--coral); letter-spacing: 1px; margin-top: 6px; line-height: 1; }
  .divider {
    position: absolute;
    left: 52px; width: 658px; top: 337px;
    height: 1px; background: var(--rule);
  }
  .contact {
    position: absolute;
    left: 0; width: 760px;
    top: 346px;
    text-align: center;
    font-family: "Roboto", sans-serif;
    font-size: 17px;
    color: var(--ink);
    line-height: 27px;
  }
  .contact__label { color: var(--red); }
  .contact__item + .contact__item { margin-left: 8px; }
  .band {
    position: absolute;
    left: 0; bottom: 0;
    width: 760px; height: 16px;
    background: var(--navy);
  }
</style>
</head>
<body>
  <section class="card card--front">
    <svg class="backdrop-shape" viewBox="0 0 560 400" aria-hidden="true">
      <circle cx="330" cy="200" r="190" fill="var(--navy-faint)" opacity="0.55"/>
    </svg>
    <div class="brand">
      <span class="brand__mark"></span>
      <span class="brand__rule"></span>
      <div class="brand__text">
        <span class="brand__lead">LAW OFFICE OF</span>
        <span class="brand__name">BRIAN KOLMER, PLLC</span>
        <span class="brand__place">Tucson, Arizona</span>
      </div>
    </div>
  </section>

  <section class="card card--back">
    <div class="brand">
      <span class="brand__mark"></span>
      <span class="brand__rule"></span>
      <div class="brand__text">
        <span class="brand__lead">LAW OFFICE OF</span>
        <span class="brand__name">BRIAN KOLMER, PLLC</span>
        <span class="brand__place">Tucson, Arizona</span>
      </div>
    </div>
    <div class="person">
      <p class="person__name">BRIAN KOLMER</p>
      <p class="person__role">LAWYER</p>
    </div>
    <div class="divider"></div>
    <div class="contact">
      <p><span class="contact__item"><span class="contact__label">P:</span> 520-555-0147</span><span class="contact__item"><span class="contact__label">F:</span> 520-555-0193</span></p>
      <p><span class="contact__item"><span class="contact__label">E:</span> brian@kolmer-law.example</span><span class="contact__item"><span class="contact__label">W:</span> www.kolmer-law.example</span></p>
    </div>
    <div class="band"></div>
  </section>
</body>
</html>
```